Swimming Pool Business Billboard

10' x 24' Billboard displaying company name, logo and phone number. Picture of swimming pool activity; kids playing , swimming, etc. Bullet points possibly shown: New Construction, Repairs, Weekly maintenance.

Industry/Entity Type

Swimming pool construction, repairs and maintenance.

Font styles to use
Sans Serif

Colors
0054AA
0677BA
7BADD7
CADEEF
E8F1F8

Requirements
Must have
• Rusty & Calder Pembrook, RUSTY'S POOLS & Service,
Nice to have
• Prefer to have my last name "Pembrook" above the word "POOLS" only in smaller print so that "RUSTYS POOLS" is distinguished.

```html
<!DOCTYPE html>
<html lang="en">
<head>
<meta charset="utf-8">
<title>Rusty's Pools Billboard</title>
<link rel="stylesheet" href="https://fonts.googleapis.com/css2?family=Poppins:wght@600;700;800&family=Montserrat:wght@700&family=Luckiest+Guy&display=swap">
<style>
  :root {
    --pool-deep: #0054aa;
    --pool-mid: #0677ba;
    --pool-light: #7badd7;
    --pool-pale: #cadeef;
    --pool-mist: #e8f1f8;
    --navy: #14296b;
    --ink: #1b2550;
    --sun: #f7e31c;
    --white: #ffffff;
    --pin: #e3262b;
  }
  * { box-sizing: border-box; margin: 0; padding: 0; }
  html, body { width: 947px; height: 1200px; overflow: hidden; }
  body { background: var(--mist, #eef3f8); background: #eef3f8; position: relative; font-family: "Poppins", sans-serif; }

  .billboard-frame {
    position: absolute; left: 33px; top: 417px;
    width: 880px; height: 366px;
    box-shadow: 0 6px 14px rgba(0,0,0,.25);
  }
  .billboard {
    position: absolute; left: 0; top: 0;
    width: 1282px; height: 533px;
    transform: scale(0.6864); transform-origin: 0 0;
    overflow: hidden;
    background: linear-gradient(160deg, #1f5fd1 0%, var(--pool-deep) 45%, #1a49b8 100%);
  }

  .brand-mark {
    position: absolute; left: 40px; top: 40px; width: 170px; height: 200px;
    display: flex; flex-direction: column; align-items: center; justify-content: center; gap: 14px;
  }
  .brand-mark .dot { width: 70px; height: 70px; border-radius: 50%; background: var(--pool-pale); }
  .brand-mark .name {
    font-weight: 800; font-size: 30px; line-height: 1.05; color: var(--white); text-align: center;
  }

  .headline { position: absolute; left: 225px; width: 730px; text-align: center; }
  .headline-owners-first {
    top: 40px; font-weight: 800; font-size: 64px; line-height: 1; color: #9fe6f2;
    -webkit-text-stroke: 2px var(--navy); paint-order: stroke fill;
    text-shadow: 0 4px 0 var(--navy);
  }
  .headline-owners-last {
    top: 107px; font-weight: 800; font-size: 68px; line-height: 1; color: var(--sun);
    letter-spacing: -1px; text-shadow: 0 4px 0 var(--navy);
  }
  .headline-company {
    top: 176px; font-family: "Luckiest Guy", sans-serif; font-size: 80px; line-height: 1;
    letter-spacing: 3px; color: #aeeaf7;
    -webkit-text-stroke: 3px var(--navy); paint-order: stroke fill;
    text-shadow: 0 5px 0 var(--navy);
  }

  .white-band { position: absolute; left: 0; top: 240px; width: 1282px; height: 160px; }

  .services-title {
    position: absolute; left: 200px; width: 620px; top: 302px; text-align: center;
    font-weight: 700; font-size: 31px; letter-spacing: 7px; color: var(--ink);
  }
  .service-pills { position: absolute; top: 348px; left: 70px; display: flex; gap: 4px; }
  .service-pill {
    height: 48px; padding: 0 28px; border: 2px solid var(--ink); border-radius: 24px;
    background: var(--white); display: flex; align-items: center;
    font-weight: 800; font-size: 31px; color: var(--ink); letter-spacing: .5px;
  }
  .service-pill.construction { width: 335px; }
  .service-pill.repairs { width: 186px; justify-content: center; }
  .service-pill.maintenance { width: 318px; justify-content: center; }

  .address-band {
    position: absolute; left: 0; top: 390px; width: 1282px; height: 52px; background: var(--sun);
    display: flex; align-items: center; padding-left: 105px; gap: 8px;
    font-weight: 800; font-size: 36px; color: var(--ink);
  }

  .photo-circle {
    position: absolute; left: 945px; top: 8px; width: 460px; height: 460px; border-radius: 50%;
    border: 12px solid var(--pool-light);
    background: radial-gradient(circle at 45% 35%, #bfe9f7 0%, #5fc0ea 45%, #3aa7dc 70%, #a5e23c 88%);
  }

  .contact-band {
    position: absolute; left: 0; top: 448px; width: 1282px; height: 85px;
    background: linear-gradient(90deg, #0f3a93, #12409f 50%, #0f3a93);
    display: flex; align-items: center; padding-left: 68px; gap: 18px;
    color: var(--white); font-family: "Montserrat", sans-serif; font-weight: 700;
  }
  .contact-phone { font-family: "Poppins", sans-serif; font-weight: 600; font-size: 50px; margin-right: 18px; }
  .contact-email { font-size: 52px; }
</style>
</head>
<body>
  <div class="billboard-frame">
    <div class="billboard">
      <div class="brand-mark">
        <span class="dot"></span>
        <span class="name">Rusty's Pools</span>
      </div>

      <div class="headline headline-owners-first">RUSTY &amp;</div>
      <div class="headline headline-owners-last">CALDER PEMBROOK</div>
      <div class="headline headline-company">RUSTY'S POOLS</div>

      <svg class="white-band" viewBox="0 0 1282 160" aria-hidden="true">
        <path d="M0 30 q32 -30 64 0 t64 0 t64 0 t64 0 t64 0 t64 0 t64 0 t64 0 t64 0 t64 0 t64 0 t64 0 t64 0 t64 0 t64 0 t64 0 t64 0 t64 0 t64 0 t64 0 V160 H0 Z" fill="#ffffff" stroke="#7badd7" stroke-width="6"/>
      </svg>

      <div class="services-title">SWIMMING POOL</div>
      <div class="service-pills">
        <div class="service-pill construction">CONSTRUCTION</div>
        <div class="service-pill repairs">REPAIRS</div>
        <div class="service-pill maintenance">MAINTENANCE</div>
      </div>

      <div class="address-band">
        <svg width="26" height="36" viewBox="0 0 26 36" aria-hidden="true">
          <path d="M13 0 C5.8 0 0 5.6 0 12.6 C0 22 13 36 13 36 S26 22 26 12.6 C26 5.6 20.2 0 13 0Z" fill="var(--pin)"/>
          <circle cx="13" cy="12.5" r="5" fill="#fff"/>
        </svg>
        <span>2750 Larkmoor Rd Fernhaven, GA 30999</span>
      </div>

      <div class="photo-circle" role="img" aria-label="Photo of smiling children floating on inflatable rings in a blue swimming pool"></div>

      <div class="contact-band">
        <svg width="44" height="44" viewBox="0 0 24 24" aria-hidden="true">
          <path d="M6.6 10.8a15.1 15.1 0 0 0 6.6 6.6l2.2-2.2a1 1 0 0 1 1-.25 11.4 11.4 0 0 0 3.6.57 1 1 0 0 1 1 1V20a1 1 0 0 1-1 1A17 17 0 0 1 3 4a1 1 0 0 1 1-1h3.5a1 1 0 0 1 1 1c0 1.25.2 2.45.57 3.57a1 1 0 0 1-.25 1z" fill="#7badd7"/>
        </svg>
        <span class="contact-phone">555-014-2276</span>
        <svg width="40" height="40" viewBox="0 0 24 24" aria-hidden="true">
          <circle cx="12" cy="12" r="10" fill="none" stroke="#7badd7" stroke-width="1.8"/>
          <ellipse cx="12" cy="12" rx="4.5" ry="10" fill="none" stroke="#7badd7" stroke-width="1.5"/>
          <path d="M2 12h20M4 7h16M4 17h16" stroke="#7badd7" stroke-width="1.5"/>
        </svg>
        <span class="contact-email">rusty@rcpools.net</span>
      </div>
    </div>
  </div>
</body>
</html>
```